Plum Vantage - Graphic Label

Company Name: Verdant Kinship
Product: Organic Energy Drink
Name of Drink : Plum Vantage
8.45oz - Bottle
http://www.tradevoxa.com/product-detail/Popular-sale-aluminum-energy-drink-bottle_4827310659.html?s=p
Attached will be examples of labels for other drinks associated with this company along with company logo. I'm open to all interpretations of design. Please submit creative ideas and we can adjust design as we go.
Design must have some integration of the geometry as seen in labels attached.
Keep it classy
If you have a vision for the design, just create it and we can adjust from there.
I want the bottle to have long lasting but creative/interesting design..
Please continue submissions.
- Thanks
Target Market(s)
All Ages .. those interested in Organics, health drinks, energy drinks
Industry/Entity Type
It Company
Look and feel

```html
<!DOCTYPE html>
<html lang="en">
<head>
<meta charset="utf-8">
<title>Plum Vantage – Energy Drink Label</title>
<link rel="stylesheet" href="https://fonts.googleapis.com/css2?family=Archivo:wght@500;700;800&family=Jura:wght@500;700&display=swap">
<style>
  :root {
    --stage: #dcdcdc;
    --label: #554b4a;
    --blue: #3f86c8;
    --white: #ffffff;
    --panel: #d9d9d9;
    --soft: #e8e4e2;
    --berry-dark: #1c1d26;
    --berry-mid: #4a4b5c;
  }
  * { margin: 0; padding: 0; box-sizing: border-box; }
  html, body { width: 1200px; height: 724px; overflow: hidden; background: var(--stage); }
  .canvas { position: relative; width: 1200px; height: 724px; }
  .label {
    position: absolute; left: 114px; top: 0;
    width: 993px; height: 740px;
    background: var(--label);
    transform: scale(0.978); transform-origin: top left;
    font-family: "Archivo", sans-serif; color: var(--white);
  }
  .label__notch { position: absolute; right: 0; bottom: 0; width: 28px; height: 17px; background: var(--stage); }
  .geometry { position: absolute; inset: 0; width: 993px; height: 740px; }
  .shake { position: absolute; left: 364px; top: 2px; transform: translateX(-50%); white-space: nowrap; font-weight: 700; font-size: 22px; letter-spacing: -0.5px; }
  .title-top { position: absolute; left: 194px; top: 110px; font-weight: 800; font-size: 88px; letter-spacing: -5px; line-height: 1; white-space: nowrap; }
  .title-main { position: absolute; left: 282px; top: 190px; font-weight: 800; font-size: 84px; letter-spacing: -5px; line-height: 1; color: var(--blue); white-space: nowrap; }
  .subtitle { position: absolute; right: 461px; top: 264px; font-weight: 700; font-size: 28px; letter-spacing: -1px; white-space: nowrap; }
  .brand { position: absolute; left: 230px; top: 606px; width: 270px; display: flex; align-items: center; justify-content: center; gap: 10px; font-weight: 700; font-size: 28px; letter-spacing: -1px; color: var(--blue); white-space: nowrap; }
  .brand__dot { width: 16px; height: 16px; border-radius: 50%; background: var(--blue); flex: none; }
  .volume { position: absolute; left: 292px; top: 676px; font-weight: 700; font-size: 15px; color: var(--soft); letter-spacing: 0.3px; white-space: nowrap; }
  .panel-window { position: absolute; left: 744px; top: 10px; width: 235px; height: 412px; background: var(--panel); }
  .panel-box { position: absolute; left: 745px; top: 540px; width: 85px; height: 138px; background: var(--panel); }
  .fine { font-family: "Jura", sans-serif; color: var(--soft); }
  .ingredients { position: absolute; left: 745px; top: 426px; width: 234px; height: 110px; font-size: 9.2px; line-height: 12.2px; letter-spacing: 0.7px; text-align: justify; }
  .caution { position: absolute; left: 836px; top: 543px; width: 146px; }
  .caution__head { font-size: 10px; font-weight: 700; letter-spacing: 0.6px; line-height: 11px; }
  .caution__body { font-size: 7.4px; line-height: 10px; margin-top: 2px; }
  .caution__rights { font-size: 10px; line-height: 12px; margin-top: 6px; letter-spacing: 0.6px; }
  .distributor { position: absolute; left: 745px; top: 688px; font-size: 10.5px; line-height: 12px; letter-spacing: 1.2px; white-space: nowrap; }
</style>
</head>
<body>
<main class="canvas">
  <section class="label" aria-label="Plum Vantage bottle label">
    <svg class="geometry" viewBox="0 0 993 740">
      <defs>
        <linearGradient id="berry-tone" x1="0" y1="0" x2="1" y2="1">
          <stop offset="0" stop-color="#4a4b5c"/>
          <stop offset="0.5" stop-color="#1c1d26"/>
          <stop offset="1" stop-color="#4a4b5c"/>
        </linearGradient>
      </defs>
      <polygon points="145,243 603,360 603,530 145,413" fill="none" stroke="var(--blue)" stroke-width="6"/>
      <polygon class="berry-band" role="img" aria-label="Close-up photo of dark purple berries" points="147,245 600,362 600,528 147,411" fill="url(#berry-tone)"/>
      <g fill="var(--blue)">
        <rect x="10" y="14" width="67" height="66"/>
        <rect x="10" y="146" width="67" height="66"/>
        <rect x="144" y="278" width="66" height="66"/>
        <rect x="77" y="345" width="66" height="66"/>
        <rect x="539" y="329" width="66" height="66"/>
        <rect x="539" y="462" width="66" height="66"/>
        <rect x="672" y="594" width="66" height="66"/>
      </g>
      <g fill="var(--white)">
        <rect x="77" y="80" width="66" height="66"/>
        <rect x="77" y="212" width="66" height="66"/>
        <rect x="606" y="396" width="66" height="66"/>
        <rect x="606" y="529" width="66" height="66"/>
        <rect x="606" y="660" width="66" height="66"/>
      </g>
      <circle class="cert-badge" cx="567" cy="566" r="29" fill="#c9c9c9"/>
      <circle cx="567" cy="566" r="27" fill="#3a3a3a"/>
    </svg>

    <p class="shake">shake well</p>
    <h1 class="title-top">Plum</h1>
    <h1 class="title-main">Vantage</h1>
    <p class="subtitle">energy drink</p>

    <div class="brand"><span class="brand__dot"></span><span>Verdant Kinship</span></div>
    <p class="volume">8.4 FL. OZ. (250mL)</p>

    <div class="panel-window"></div>
    <p class="fine ingredients">Ingredients: Carbonated Water, Sucrose, Glucose, Citric Acid, Taurine, Sodium Citrate, Natural &amp; Artificial Flavors, Color Added, Caffeine, Glucuronolactone, Potassium Sorbate, Sodium Benzoate, Guarana Seed Extract, Panax Ginseng Extract, Niacinamide, Inositol, L-Carnitine, Pyridoxine Hydrochloride, Calcium Pantothenate, Cyanocobalamin.</p>

    <div class="panel-box"></div>
    <div class="fine caution">
      <p class="caution__head">CAUTION: CONSUME RESPONSIBLY</p>
      <p class="caution__body">Limit or avoid products containing caffeine to avoid jitters, sleeplessness and rapid heartbeat. Not for use by individuals under 18 years of age, pregnant or nursing, or those sensitive to caffeine.</p>
      <p class="caution__rights">© 2013 ????????<br>All rights reserved</p>
    </div>

    <p class="fine distributor">Distributed By: ?????????????????<br>City, State Zip<br>Phone #<br>www.yourwebsitename.com</p>

    <div class="label__notch"></div>
  </section>
</main>
</body>
</html>
```